Historic Church website

We want our church website to feel warm, historic, and clean, modern, and easy to navigate. Dont use the anchor

Current website: https://www.meadowlarkfellowship.org/

Requirements
Should not have
• I would like to use the logo without the anchor

```html
<!DOCTYPE html>
<html lang="en">
<head>
<meta charset="utf-8">
<title>Meadowlark Fellowship</title>
<link href="https://fonts.googleapis.com/css2?family=Cormorant+Garamond:ital,wght@0,400;0,500;0,600;1,400&family=EB+Garamond:wght@400;500&display=swap" rel="stylesheet">
<style>
:root{
  --gold:#c9a13b;
  --gold-soft:#a88a3c;
  --ink:#f1ebe0;
  --muted:#8c8273;
  --dim:#5f574c;
  --bg-deep:#0f0c0a;
  --bg-mid:#17130f;
  --bg-bar:#2a211b;
  --bg-foot:#271e19;
  --card:#221c17;
  --field:#241e19;
  --line:#3a3129;
}
*{margin:0;padding:0;box-sizing:border-box}
html,body{width:1200px;height:1200px;overflow:hidden;background:#fff}
.page{position:absolute;left:430px;top:0;width:548px;height:1932px;transform:scale(.6211);transform-origin:0 0;font-family:"EB Garamond",serif;color:var(--ink);background:var(--bg-deep)}
.band{position:absolute;left:0;width:548px}
.abs{position:absolute}
.center{left:0;width:548px;text-align:center}
.display{font-family:"Cormorant Garamond",serif;font-weight:500}

.topbar{top:0;height:13px;background:var(--bg-bar);font-size:4px;color:var(--muted)}
.topbar .left{left:36px;top:4px}
.topbar .right{right:36px;top:4px;color:var(--gold)}

.nav{top:13px;height:34px;background:#1d1713}
.brand{left:36px;top:8px;display:flex;align-items:center;gap:5px}
.brand .dot{width:12px;height:12px;border-radius:50%;border:1px solid var(--gold)}
.brand .name{font-size:8px;line-height:1}
.menu{right:36px;top:10px;display:flex;align-items:center;gap:13px;font-size:4.6px;color:#d8d0c2}
.donate{background:var(--gold);color:#1a140f;padding:4px 6px}

.hero{top:47px;height:216px;background:radial-gradient(ellipse at 50% 30%,#4a3626 0%,#2a1d14 55%,#150f0b 100%)}
.hero .rule{top:10px;left:236px;width:76px;height:1px;background:var(--gold-soft)}
.hero .mark{top:7px;left:270px;width:8px;height:8px;border:1px solid var(--gold);border-radius:50%;background:#2a1d14}
.hero h1{top:30px;font-size:26px;line-height:34.5px;font-weight:500}
.hero h1 .gold{color:var(--gold)}
.hero .verse{top:145px;font-size:6px;color:#d6cdbd}
.hero .ref{top:160px;font-size:5px;color:var(--gold)}
.btn{position:absolute;height:18px;font-size:5.6px;display:flex;align-items:center;justify-content:center}
.btn.solid{background:var(--gold);color:#1a140f}
.btn.ghost{border:1px solid #6e6355;color:#e8e0d2}

.newsletter{top:263px;height:222px;background:var(--bg-mid)}
.divider{position:absolute;height:1px;background:var(--gold-soft)}
.icon-sm{position:absolute;width:8px;height:7px}
.h2{font-size:13px;font-weight:500}
.sub{font-size:4.6px;color:var(--dim)}
.label{font-size:4px;color:#b7ad9d}
.field{position:absolute;height:13px;background:var(--field);font-size:4.4px;color:#6d6356;padding:4px 5px}
.help{font-size:3.4px;color:#6a6155}
.send{position:absolute;left:245px;top:177px;width:58px;height:13px;background:var(--gold);color:#1a140f;font-size:4.6px;display:flex;align-items:center;justify-content:center}

.about{top:485px;height:255px;background:var(--bg-deep)}
.photo{position:absolute}
.about .photo{left:36px;top:42px;width:229px;height:171px;background:linear-gradient(160deg,#3a2a1e,#6a4a2c 45%,#2a1d15)}
.about .heading{left:283px;top:50px;width:230px;font-size:12.5px;line-height:15px;font-weight:500}
.about .body{left:283px;top:104px;width:230px;font-size:4.5px;line-height:10px;color:#b9af9f}
.about .body p{margin-bottom:6px}

.visit{top:740px;height:453px;background:var(--bg-mid)}
.pill{position:absolute;left:196px;top:31px;width:157px;height:13px;border-radius:7px;background:#2a231c;font-size:3.8px;color:var(--gold);display:flex;align-items:center;justify-content:center;gap:3px}
.card{position:absolute;top:100px;width:128px;height:105px;background:var(--card);text-align:center;padding-top:13px}
.card.active{border:1px solid var(--gold);background:#1c1712}
.card .clock{display:block;margin:0 auto}
.card .title{font-size:6.4px;margin-top:6px}
.card .time{font-size:8px;color:var(--gold);margin-top:5px}
.card .desc{font-size:3.8px;color:#6f665a;line-height:7px;margin:8px 14px 0}
.card .chev{font-size:7px;color:var(--gold);margin-top:3px}
.visit .photo{left:103px;top:231px;width:342px;height:191px;background:linear-gradient(110deg,#5c5c5e,#a89f93 40%,#c6bcae 70%,#8d949a)}
.visit .caption{left:112px;top:405px;font-size:6px;color:#fff}

.events{top:1193px;height:367px;background:var(--bg-deep)}
.events .photo{left:36px;top:31px;width:229px;height:305px;background:radial-gradient(circle at 38% 40%,#d99a52,#5a3b24 30%,#2b1e16 70%)}
.events .title{left:283px;top:31px;font-size:13px;display:flex;align-items:center;gap:5px}
.event{position:absolute;left:290px;width:222px;height:37px;border-bottom:1px solid #1f1a15}
.event .day{position:absolute;left:0;top:0;width:12px;text-align:center;font-size:3.4px;color:var(--gold);line-height:5px}
.event .day b{display:block;font-size:7px;color:var(--ink);font-weight:500;line-height:8px}
.event .day i{font-style:normal;color:#6a6155}
.event .hour{position:absolute;left:27px;top:4px;font-size:3.6px;color:var(--gold)}
.event .what{position:absolute;left:27px;top:10px;font-size:5px}
.event .go{position:absolute;right:2px;top:5px;font-size:7px;color:var(--gold)}
.events .addcal{left:290px;top:291px;font-size:4.4px;color:var(--gold)}
.events .viewcal{position:absolute;left:461px;top:288px;width:51px;height:13px;border:1px solid #6e6355;font-size:4.4px;display:flex;align-items:center;justify-content:center}

.quote{top:1560px;height:190px;background:var(--bg-mid)}
.quote .qm{top:32px;font-size:32px;color:var(--gold-soft);line-height:1}
.quote blockquote{position:absolute;left:100px;width:348px;top:67px;font-family:"Cormorant Garamond",serif;font-style:italic;font-size:11px;line-height:18.5px;text-align:center;color:#e6ddcc}
.quote .who{top:141px;font-size:6px;color:var(--gold)}

.footer{top:1750px;height:182px;background:var(--bg-foot)}
.footer .brand{top:24px}
.fcol{position:absolute;top:24px;font-size:4px;color:#978c7c;line-height:6px}
.fcol h4{font-size:5.6px;color:var(--ink);font-weight:500;margin-bottom:10px}
.fcol .item{margin-bottom:6px}
.fcol .item b{display:block;color:#d5ccbc;font-weight:400}
.fcol .link{margin-bottom:6px}
.contact{position:absolute;left:36px;top:52px;font-size:3.8px;color:#978c7c;line-height:6px}
.contact div{display:flex;gap:5px;margin-bottom:6px}
.socials{position:absolute;left:36px;top:100px;display:flex;gap:6px}
.socials span{width:6px;height:6px;border:1px solid #8c8273;border-radius:50%}
.footer .legal{top:152px;font-size:3.8px;color:#6e6457}
.footer .legal.left{left:36px}
.footer .legal.right{right:36px}
</style>
</head>
<body>
<div class="page">

  <div class="band topbar">
    <div class="abs left">2840 Larkspur Avenue, Fairhaven, CA &nbsp;&nbsp;&nbsp; 555-014-2290</div>
    <div class="abs right">info@meadowlarkfellowship.org</div>
  </div>

  <header class="band nav">
    <div class="abs brand"><span class="dot"></span><span class="name display">Meadowlark Fellowship</span></div>
    <nav class="abs menu">
      <span>Home</span><span>About MF ⌄</span><span>Ministries ⌄</span><span>Bible Studies ⌄</span><span>Sermon Library</span><span class="donate">Donate</span>
    </nav>
  </header>

  <section class="band hero" role="img" aria-label="Dim historic library with tall wooden bookshelves and a ladder">
    <div class="abs rule"></div><div class="abs mark"></div>
    <h1 class="abs center display">Ancient Church.<br><span class="gold">Ancient Faith.</span><br>Eternal Truth.</h1>
    <p class="abs center verse">“We have this hope as an anchor for the soul, firm and secure.”</p>
    <p class="abs center ref">— Hebrews 6:19</p>
    <a class="btn solid" style="left:196px;top:188px;width:82px">Join Our Community</a>
    <a class="btn ghost" style="left:285px;top:188px;width:67px">Watch Sermons</a>
  </section>

  <section class="band newsletter">
    <div class="divider" style="left:246px;top:35px;width:18px"></div>
    <div class="divider" style="left:284px;top:35px;width:18px"></div>
    <svg class="icon-sm" style="left:270px;top:31px" viewBox="0 0 8 7"><rect x=".5" y=".5" width="7" height="6" fill="none" stroke="#c9a13b" stroke-width=".8"/><path d="M.5 .8 4 3.8 7.5 .8" fill="none" stroke="#c9a13b" stroke-width=".8"/></svg>
    <h2 class="abs center h2 display" style="top:49px">Sign Up for Our Weekly Newsletter</h2>
    <p class="abs center sub" style="top:72px">Stay connected with our community and receive weekly updates, devotionals, and announcements.</p>
    <div class="abs label" style="left:128px;top:96px">First Name *</div>
    <div class="abs label" style="left:277px;top:96px">Last Name *</div>
    <div class="field" style="left:128px;top:106px;width:143px">Enter your first name</div>
    <div class="field" style="left:277px;top:106px;width:143px">Enter your last name</div>
    <div class="abs help" style="left:137px;top:123px">So We Know Who to Write To</div>
    <div class="abs help" style="left:286px;top:123px">So We Know Who to Write To</div>
    <div class="abs label" style="left:128px;top:135px">Email *</div>
    <div class="field" style="left:128px;top:145px;width:292px">Enter your email address</div>
    <div class="abs help" style="left:137px;top:163px">This Email Is Where You Will Receive Our Newsletter</div>
    <a class="send">Click to Send</a>
  </section>

  <section class="band about">
    <div class="photo" role="img" aria-label="Warm study room with bookshelves, fireplace, leather armchairs and a framed map"></div>
    <svg class="icon-sm" style="left:283px;top:30px" viewBox="0 0 8 7"><path d="M.5 1h3v5.5h-3zM4.5 1h3v5.5h-3z" fill="none" stroke="#c9a13b" stroke-width=".8"/></svg>
    <div class="divider" style="left:296px;top:34px;width:217px;background:#3a3129"></div>
    <h2 class="abs heading display">Meadowlark Fellowship is an independent Christian church in the Protestant tradition.</h2>
    <div class="abs body">
      <p>Its central tenets are found in its Statement of Faith and include belief in the Deity and Lordship of Jesus Christ; the Trinity; Jesus' perfect life, atoning death on the cross, bodily resurrection, and ascension; Jesus' literal return; the inerrancy of the Bible in its original manuscripts; and our need for salvation through personal faith in Jesus Christ.</p>
      <p>The church is historic in that it recognizes the creeping apostasy of the church during the centuries immediately following the Apostles; we teach Premillennialism. That is, the belief that Messiah will physically and literally return to earth in Jerusalem before the millennial age commences; at that time, he will establish a kingdom over which he will preside as King.</p>
      <p>All the promises of Israel's covenants will be literally fulfilled during this reign. At the end of one thousand years, the kingdom will be transferred from the Son to the Father (1 Cor 15:24-25) and it will merge with the eternal kingdom (Rev 20-22).</p>
    </div>
  </section>

  <section class="band visit">
    <div class="pill"><span>▷</span> If you cannot join us in person, click here for this week's sermon</div>
    <h2 class="abs center h2 display" style="top:53px">Visit Us This Sunday</h2>
    <p class="abs center sub" style="top:76px">Flip the boxes for more information</p>

    <div class="card active" style="left:76px">
      <svg class="clock" width="11" height="11" viewBox="0 0 11 11"><circle cx="5.5" cy="5.5" r="4.8" fill="none" stroke="#c9a13b" stroke-width=".8"/><path d="M5.5 2.8v2.9l1.8 1.1" fill="none" stroke="#c9a13b" stroke-width=".8"/></svg>
      <div class="title">Morning Worship Service</div><div class="time">10:00 AM</div>
      <div class="desc">Join us for worship, prayer, and the preaching of God's Word.</div><div class="chev">›</div>
    </div>
    <div class="card" style="left:210px;top:102px;height:103px">
      <svg class="clock" width="11" height="11" viewBox="0 0 11 11"><circle cx="5.5" cy="5.5" r="4.8" fill="none" stroke="#c9a13b" stroke-width=".8"/><path d="M5.5 2.8v2.9l1.8 1.1" fill="none" stroke="#c9a13b" stroke-width=".8"/></svg>
      <div class="title">All Church Lunch</div><div class="time">12:15 PM</div>
      <div class="desc">Fellowship together as a church family over a shared meal.</div><div class="chev">›</div>
    </div>
    <div class="card" style="left:345px;top:102px;height:103px;width:125px">
      <svg class="clock" width="11" height="11" viewBox="0 0 11 11"><circle cx="5.5" cy="5.5" r="4.8" fill="none" stroke="#c9a13b" stroke-width=".8"/><path d="M5.5 2.8v2.9l1.8 1.1" fill="none" stroke="#c9a13b" stroke-width=".8"/></svg>
      <div class="title">Afternoon Adult Bible Study</div><div class="time">12:45 PM</div>
      <div class="desc">In-depth study of Scripture for spiritual growth.</div><div class="chev">›</div>
    </div>

    <div class="photo" role="img" aria-label="Exterior of the church building with arched doorway beside a tall apartment tower"></div>
    <div class="abs caption">2840 Larkspur Avenue, Fairhaven, California</div>
  </section>

  <section class="band events">
    <div class="photo" role="img" aria-label="Glowing lantern on a wooden table in a softly lit room"></div>
    <h2 class="abs title display"><svg width="8" height="8" viewBox="0 0 8 8"><rect x=".5" y="1.2" width="7" height="6.3" fill="none" stroke="#c9a13b" stroke-width=".8"/><path d="M.5 3h7M2.3.3v1.6M5.7.3v1.6" stroke="#c9a13b" stroke-width=".8"/></svg>Upcoming MF Events</h2>

    <div class="event" style="top:63px"><div class="day">SUN<b>18</b><i>Jan</i></div><div class="hour">11:00 am</div><div class="what">Sunday Service</div><div class="go">›</div></div>
    <div class="event" style="top:100px"><div class="day">WED<b>21</b><i>Jan</i></div><div class="hour">7:30 pm</div><div class="what">Wednesday Night Bible Study</div><div class="go">›</div></div>
    <div class="event" style="top:137px"><div class="day">SUN<b>25</b><i>Jan</i></div><div class="hour">11:00 am</div><div class="what">Sunday Service</div><div class="go">›</div></div>
    <div class="event" style="top:174px"><div class="day">WED<b>28</b><i>Jan</i></div><div class="hour">7:30 pm</div><div class="what">Wednesday Night Bible Study</div><div class="go">›</div></div>
    <div class="event" style="top:211px"><div class="day">SUN<b>1</b><i>Feb</i></div><div class="hour">11:00 am</div><div class="what">Sunday Service</div><div class="go">›</div></div>
    <div class="event" style="top:248px"><div class="day">WED<b>4</b><i>Feb</i></div><div class="hour">7:30 pm</div><div class="what">Wednesday Night Bible Study</div><div class="go">›</div></div>

    <div class="abs addcal">Add to Calendar</div>
    <a class="viewcal">View Calendar →</a>
  </section>

  <section class="band quote">
    <div class="abs center qm display">”</div>
    <blockquote>"Christians are called to God's service not only in church professions but also in every secular calling. The task of restoring truth to the culture depends largely on our laypeople."</blockquote>
    <div class="divider" style="left:262px;top:133px;width:24px"></div>
    <div class="abs center who">Elias Thornbury</div>
  </section>

  <footer class="band footer">
    <div class="abs brand"><span class="dot"></span><span class="name display">Meadowlark Fellowship</span></div>
    <div class="contact">
      <div><span style="color:#c9a13b">●</span><span>2840 Larkspur Avenue<br>Fairhaven, California 90210</span></div>
      <div><span style="color:#c9a13b">●</span><span>555-014-2290</span></div>
      <div><span style="color:#c9a13b">●</span><span>info@meadowlarkfellowship.org</span></div>
    </div>
    <div class="socials"><span></span><span></span><span></span><span></span></div>

    <div class="fcol" style="left:159px">
      <h4>MF Sermons</h4>
      <div class="item"><b>A Plain Song For a Perplexed World</b>January 11, 2026<br>Meadowlark Fellowship</div>
      <div class="item"><b>The Lion and His Lamb Reigns</b>January 4, 2026<br>Meadowlark Fellowship</div>
      <div class="item"><b>The Kingdom is Coming</b>December 28, 2025<br>Meadowlark Fellowship</div>
    </div>
    <div class="fcol" style="left:283px">
      <h4>Quick Links</h4>
      <div class="link">› Home</div><div class="link">› Bible Church</div><div class="link">› Our Affirmations</div><div class="link">› Sermons</div><div class="link">› Donate</div>
    </div>
    <div class="fcol" style="left:405px;top:42px">
      <div class="link">› Visiting on a Sunday</div><div class="link">› Events Calendar</div><div class="link">› Sunday Bible Studies</div><div class="link">› Contact Us</div>
    </div>

    <div class="abs legal left">© Copyright 2026 – Meadowlark Fellowship, Fairhaven, California</div>
    <div class="abs legal right">All Rights Reserved</div>
  </footer>

</div>
</body>
</html>
```